Business card design for sports medicine and athlete care clinic.

We need a bold, solid business card design for our practitioners to stand out. We treat overuse & sports-related injuries and provide post-operative rehabilitation. Our specialisations include chronic conditions, men’s health, nutrition & musculoskeletal disorders (MSDs). All brand collateral in terms of fonts, logo and colour palette to be provided.

Target Market(s)

Athletes (professional and amateur), sportspeople, predominantly male

Industry/Entity Type

Health And Wellness

Contact Information for Business Card

The front of the card should be white with dark blue text the back dark blue with white text. The logo should be top-left. The business name should be horizontal and right of the logo. The tagline should be directly below centred on the back of the card (see top-banner.png and bottom-banner.png)

Font styles to use
Sans Serif

Colors
0355a3
0293ce
3176b5
ffffff
85acd3

Requirements
Nice to have
• Diagonal and/or horizontal line elements between logo and practitioner details and/or bottom corner of card (see slide.png and tag-bg.png).

```html
<!DOCTYPE html>
<html lang="en">
<head>
<meta charset="utf-8">
<title>The Runner's League – Business Card</title>
<link rel="stylesheet" href="https://fonts.googleapis.com/css2?family=Montserrat:wght@300;400;500;700;800&display=swap">
<style>
  :root {
    --navy: #1f2157;
    --blue: #1a8fd0;
    --cyan: #27b4e6;
    --sky: #85acd3;
    --white: #ffffff;
    --ink: #1f2157;
    --stage: #1b1b1e;
  }
  * { margin: 0; padding: 0; box-sizing: border-box; }
  html, body {
    width: 1200px; height: 948px; overflow: hidden;
    background: var(--stage);
    font-family: "Montserrat", sans-serif;
  }
  .canvas { position: relative; width: 1200px; height: 948px; }
  .card {
    position: absolute; left: 230px; width: 740px; height: 423px;
    border-radius: 28px; overflow: hidden;
  }

  /* Navy side with white type */
  .card--back { top: 31px; background: var(--navy); }
  .back__figure {
    position: absolute; left: 80px; top: 40px; width: 240px; height: 345px;
    border-radius: 120px 120px 60px 60px;
    background: radial-gradient(ellipse at 50% 45%, var(--cyan) 0%, var(--blue) 55%, rgba(26,143,208,0) 100%);
    opacity: .85;
  }
  .back__brand {
    position: absolute; left: 350px; top: 170px; width: 360px;
    color: var(--white); text-align: center;
  }
  .back__name { font-weight: 800; font-size: 30px; letter-spacing: .3px; white-space: nowrap; }
  .back__tagline { margin-top: 8px; font-weight: 500; font-size: 13px; letter-spacing: 2px; white-space: nowrap; }

  /* White side with navy type */
  .card--front { top: 494px; background: var(--white); }
  .front__band { position: absolute; left: 0; top: 0; width: 740px; height: 423px; }
  .front__person { position: absolute; right: 40px; top: 32px; text-align: right; color: var(--white); }
  .person__name { font-weight: 800; font-size: 24px; letter-spacing: .5px; }
  .person__role { font-weight: 400; font-size: 14px; margin-top: 2px; }

  .front__brand {
    position: absolute; left: 96px; top: 232px; display: flex; align-items: center; gap: 12px;
  }
  .brand__dot { width: 30px; height: 30px; border-radius: 50%; background: var(--blue); flex: none; }
  .brand__name { font-weight: 800; font-size: 24px; color: var(--ink); white-space: nowrap; line-height: 1.1; }
  .brand__tagline { font-weight: 500; font-size: 10px; letter-spacing: 1.8px; color: var(--blue); margin-top: 3px; white-space: nowrap; }

  .front__contacts {
    position: absolute; left: 110px; top: 294px; list-style: none; color: var(--ink);
    font-weight: 300; font-size: 16px; line-height: 27px;
  }
  .contact { display: flex; align-items: center; gap: 12px; white-space: nowrap; }
  .contact__icon { width: 15px; height: 15px; flex: none; }
  .contact__social-dot { width: 14px; height: 14px; border-radius: 50%; background: var(--cyan); flex: none; margin: 0 1px; }

  .front__figure {
    position: absolute; left: 560px; top: 140px; width: 140px; height: 235px;
    border-radius: 70px 70px 40px 40px;
    background: radial-gradient(ellipse at 50% 45%, var(--cyan) 0%, var(--blue) 55%, rgba(26,143,208,0) 100%);
    opacity: .8;
  }
</style>
</head>
<body>
<main class="canvas">

  <section class="card card--back" aria-label="Card back">
    <div class="back__figure" role="img" aria-label="Athlete figure brand illustration"></div>
    <div class="back__brand">
      <div class="back__name">The Runner's League</div>
      <div class="back__tagline">Sports medicine and athlete care</div>
    </div>
  </section>

  <section class="card card--front" aria-label="Card front">
    <svg class="front__band" viewBox="0 0 740 423" aria-hidden="true">
      <path d="M0 0 H740 V78 C180 158 35 212 0 296 Z" fill="var(--blue)"/>
      <path d="M0 0 H740 V78 C180 148 30 196 0 268 Z" fill="var(--navy)"/>
    </svg>

    <div class="front__person">
      <div class="person__name">DANIEL HART</div>
      <div class="person__role">Owner/CEO</div>
    </div>

    <div class="front__brand">
      <span class="brand__dot"></span>
      <div>
        <div class="brand__name">The Runner's League</div>
        <div class="brand__tagline">Sports medicine and athlete care</div>
      </div>
    </div>

    <ul class="front__contacts">
      <li class="contact">
        <svg class="contact__icon" viewBox="0 0 16 16"><path d="M4 1.5 6 5 4.6 6.4c.8 1.7 2.2 3.1 3.9 3.9L10 9l3.5 2-1 2.6c-.3.6-1 .9-1.6.7C6.3 13 3 9.7 1.7 5.1c-.2-.6.1-1.3.7-1.6Z" fill="var(--cyan)"/></svg>
        <span>555-014-2290</span>
      </li>
      <li class="contact">
        <svg class="contact__icon" viewBox="0 0 16 16"><rect x="1" y="3" width="14" height="10" rx="1" fill="var(--blue)"/><path d="M1.5 3.5 8 9l6.5-5.5" fill="none" stroke="var(--white)" stroke-width="1.3"/></svg>
        <span>info@therunnersleague.com.au</span>
      </li>
      <li class="contact">
        <svg class="contact__icon" viewBox="0 0 16 16"><circle cx="8" cy="8" r="7" fill="var(--blue)"/><path d="M1 8h14M8 1c-2.5 2.2-2.5 11.8 0 14M8 1c2.5 2.2 2.5 11.8 0 14" fill="none" stroke="var(--white)" stroke-width="1"/></svg>
        <span>www.therunnersleague.com.au</span>
      </li>
      <li class="contact">
        <span class="contact__social-dot"></span>
        <span>RunnersLeagueAU</span>
      </li>
    </ul>

    <div class="front__figure" role="img" aria-label="Athlete figure brand illustration"></div>
  </section>

</main>
</body>
</html>
```